Business card & stationery for audio visual & security system installation company
Audio visual & security system installations
I need double sided standard sized Business Card [3.5" x 2"]
Up to the designer
Professional
Teodor Malsk
Suite 418, 6 -10 Quenby Street,
Kelmore Heights, NSW 2041
teodor@plenvo.com.au
www.plenvo.com.au
Master Cabler No - K519207
Logo on the front
Logo on the back

```html
<!DOCTYPE html>
<html lang="en">
<head>
<meta charset="utf-8">
<title>Plenvo — Business Card</title>
<link href="https://fonts.googleapis.com/css2?family=Exo+2:wght@400;600;800&display=swap" rel="stylesheet">
<style>
  :root{
    --page:#d9d9dc;
    --card-dark:#1c1c1e;
    --card-mid:#2f2f32;
    --chrome-light:#e9e9ec;
    --chrome-dark:#5a5a60;
    --band:#0d0d0e;
    --red:#e0141e;
    --red-bright:#ff2a34;
    --white:#f4f4f4;
    --grey-text:#b9b9bd;
  }
  *{box-sizing:border-box;margin:0;padding:0}
  html,body{width:1200px;height:874px;overflow:hidden;background:var(--page);font-family:"Exo 2",sans-serif}
  .canvas{width:1200px;height:874px;display:flex;flex-direction:column;align-items:center;justify-content:center;gap:60px}
  .card{position:relative;width:620px;height:354px;border-radius:16px;overflow:hidden;
    background:
      repeating-linear-gradient(0deg,rgba(255,255,255,.025) 0 1px,transparent 1px 3px),
      linear-gradient(160deg,var(--card-mid),var(--card-dark) 60%,#141415);
    box-shadow:0 10px 28px rgba(0,0,0,.35)}
  .band{position:absolute;left:0;right:0;height:44px;
    background:
      linear-gradient(90deg,transparent 5%,rgba(224,20,30,.55) 35%,rgba(224,20,30,.55) 65%,transparent 95%),
      var(--band);
    border-top:4px solid var(--chrome-light);border-bottom:4px solid var(--chrome-light);
    box-shadow:0 -1px 0 var(--chrome-dark),0 1px 0 var(--chrome-dark)}
  .band--top{top:34px}
  .band--bottom{bottom:28px}
  .brand{display:flex;align-items:center;gap:10px;color:var(--red);font-weight:800;letter-spacing:1px;line-height:1}
  .brand-dot{border-radius:50%;background:var(--red)}
  .front .brand{position:absolute;left:50%;top:56%;transform:translate(-50%,-50%);font-size:74px}
  .front .brand-dot{width:22px;height:22px}
  .back .brand{position:absolute;left:44px;top:104px;font-size:52px}
  .back .brand-dot{width:16px;height:16px}
  .details{position:absolute;right:40px;top:112px;text-align:right;color:var(--grey-text);font-size:12.5px;line-height:1.6}
  .name{color:var(--white);font-weight:600;font-size:22px;letter-spacing:2px;text-transform:uppercase;margin-bottom:6px}
  .contacts{position:absolute;left:44px;right:40px;bottom:96px;display:flex;justify-content:space-between;color:var(--white);font-size:12px}
  .contact{display:flex;align-items:center;gap:6px}
  .contact svg{width:14px;height:14px;flex:none}
  .web{position:absolute;left:0;right:0;bottom:36px;text-align:center;color:var(--red-bright);font-weight:600;font-size:18px;letter-spacing:6px;line-height:36px}
</style>
</head>
<body>
<main class="canvas">
  <section class="card front" aria-label="Card front">
    <div class="band band--top"></div>
    <div class="brand"><span class="brand-dot"></span>Plenvo</div>
  </section>

  <section class="card back" aria-label="Card back">
    <div class="band band--top"></div>
    <div class="brand"><span class="brand-dot"></span>Plenvo</div>
    <div class="details">
      <p class="name">Teodor Malsk</p>
      <p>Master Cabler No - K519207</p>
      <p>Suite 418, 6 -10 Quenby Street,</p>
      <p>Kelmore Heights, NSW 2041</p>
    </div>
    <div class="contacts">
      <span class="contact"><svg viewBox="0 0 14 14"><rect width="14" height="14" rx="2" fill="#e0141e"/><path d="M4 3h2l1 2-1 1c.5 1 1 1.5 2 2l1-1 2 1v2c-4 0-7-3-7-7z" fill="#fff"/></svg>02 9461 3380</span>
      <span class="contact"><svg viewBox="0 0 14 14"><rect width="14" height="14" rx="2" fill="#e0141e"/><rect x="4.5" y="2.5" width="5" height="9" rx="1" fill="none" stroke="#fff"/></svg>0432 715 264</span>
      <span class="contact"><svg viewBox="0 0 14 14"><rect width="14" height="14" rx="2" fill="#e0141e"/><rect x="3" y="5" width="8" height="5" fill="none" stroke="#fff"/><rect x="4.5" y="2.5" width="5" height="2.5" fill="#fff"/></svg>02 9461 3385</span>
      <span class="contact"><svg viewBox="0 0 14 14"><rect width="14" height="14" rx="2" fill="#e0141e"/><rect x="3" y="4" width="8" height="6" fill="none" stroke="#fff"/><path d="M3 4l4 3 4-3" fill="none" stroke="#fff"/></svg>teodor@plenvo.com.au</span>
    </div>
    <div class="band band--bottom"></div>
    <p class="web">www.plenvo.com.au</p>
  </section>
</main>
</body>
</html>
```